Door Hanger Design

I need a design for a door hanger campaign. The door hanger will be 3.5" x 8.5" full color 2 sides. On the first side the emphasis is going to be house painting, exterior and interior. I would really like this to be bold and colorful, I would like to stay away from the standard here is what a painted house looks like.

For the 2nd side I would like the emphasis to be on kitchen and bathroom remodeling. One the front page of our website is a photo of one of our best jobs and if that could be incorporated into side 2 of the door hanger that would be awesome.

The name of our business is Casa Brightwell . Our website is http://casa-brightwell.example/. We don't currently have a company logo that we use.

I have never done this type of project before. So I'm sure I may be leaving some information out. If you need any questions answered please don't hesitate to contact me. They company that is going to print the designs said that I needed "camera ready artwork" and something about high resolution files.

Industry/Entity Type

House

```html
<!DOCTYPE html>
<html lang="en">
<head>
<meta charset="utf-8">
<title>Casa Brightwell – House Painting Door Hanger</title>
<link rel="stylesheet" href="https://fonts.googleapis.com/css2?family=Arimo:wght@400;700&family=Luckiest+Guy&display=swap">
<style>
  :root {
    --page: #ffffff;
    --hanger-yellow: #fff200;
    --band-orange: #ff4312;
    --band-red: #c4001c;
    --band-violet: #5a24dc;
    --band-blue: #1f2bf0;
    --band-green: #22ee22;
    --ink: #000000;
    --brand-red: #e8331c;
    --title-yellow: #ffe600;
    --title-red: #ee1c1c;
    --title-green: #18c21b;
    --title-blue: #2233ee;
    --title-orange: #ff8a00;
    --title-violet: #8a2be2;
  }
  html, body {
    margin: 0;
    padding: 0;
    width: 1200px;
    height: 2601px;
    overflow: hidden;
    background: var(--page);
  }
  .canvas {
    position: relative;
    width: 1200px;
    height: 2601px;
  }
  .door-hanger {
    position: absolute;
    left: 171px;
    top: 195px;
    width: 849px;
    height: 2205px;
    background: var(--hanger-yellow);
    overflow: hidden;
  }
  .color-band {
    position: absolute;
    left: 0;
    width: 100%;
    display: flex;
  }
  .color-band span { flex: 1; }
  .color-band--top { top: 0; height: 159px; }
  .color-band--bottom { bottom: 0; height: 75px; }
  .swatch-orange { background: var(--band-orange); }
  .swatch-red { background: var(--band-red); }
  .swatch-violet { background: var(--band-violet); }
  .swatch-blue { background: var(--band-blue); }
  .swatch-green { background: var(--band-green); }
  .hanger-hole {
    position: absolute;
    left: 303px;
    top: 0;
    width: 252px;
    height: 252px;
    border-radius: 50%;
    background: var(--ink);
  }
  .service-scope {
    position: absolute;
    left: 54px;
    top: 335px;
    margin: 0;
    font-family: "Arimo", Arial, sans-serif;
    font-weight: 700;
    font-size: 37px;
    letter-spacing: -0.5px;
    color: var(--ink);
  }
  .headline {
    position: absolute;
    left: 50px;
    top: 400px;
    margin: 0;
    font-family: "Luckiest Guy", "Arial Black", sans-serif;
    font-weight: 400;
    line-height: 0.95;
    transform: rotate(-4deg);
    transform-origin: left top;
    -webkit-text-stroke: 4px #ffffff;
    paint-order: stroke fill;
    text-shadow: 8px 8px 0 var(--ink), 4px 4px 0 var(--ink);
  }
  .headline__line { display: block; }
  .headline__line--house { font-size: 190px; margin-left: 10px; }
  .headline__line--painting { font-size: 150px; margin-left: 40px; }
  .c-yellow { color: var(--title-yellow); }
  .c-red { color: var(--title-red); }
  .c-green { color: var(--title-green); }
  .c-blue { color: var(--title-blue); }
  .c-orange { color: var(--title-orange); }
  .c-violet { color: var(--title-violet); }
  .brush-artwork {
    position: absolute;
    left: 129px;
    top: 690px;
    width: 720px;
    height: 1050px;
    background: linear-gradient(to bottom,
      #f3e070 0%, #ff8a1a 20%, #ee2020 38%,
      #9a40e0 56%, #2a55f0 74%, #33dd33 92%, var(--hanger-yellow) 100%);
    opacity: 0.9;
  }
  .byline {
    position: absolute;
    left: 54px;
    top: 1695px;
    margin: 0;
    font-family: "Arimo", Arial, sans-serif;
    font-weight: 700;
    font-size: 50px;
    color: var(--ink);
  }
  .brand-mark {
    position: absolute;
    left: 153px;
    top: 1810px;
    width: 156px;
    height: 170px;
    background: var(--brand-red);
  }
  .brand-name {
    position: absolute;
    left: 84px;
    top: 1995px;
    margin: 0;
    font-family: "Arimo", Arial, sans-serif;
    font-weight: 400;
    font-size: 43px;
    color: var(--ink);
  }
  .web-address {
    position: absolute;
    left: 135px;
    top: 2068px;
    margin: 0;
    font-family: "Arimo", Arial, sans-serif;
    font-weight: 400;
    font-size: 35px;
    color: var(--ink);
  }
</style>
</head>
<body>
<main class="canvas">
  <section class="door-hanger">
    <div class="color-band color-band--top">
      <span class="swatch-orange"></span><span class="swatch-red"></span><span class="swatch-violet"></span><span class="swatch-blue"></span><span class="swatch-green"></span>
    </div>
    <div class="hanger-hole"></div>

    <p class="service-scope">INTERIOR or EXTERIOR</p>

    <div class="brush-artwork" role="img" aria-label="Row of paint brushes trailing drips of yellow, orange, red, purple, blue and green paint"></div>

    <h1 class="headline">
      <span class="headline__line headline__line--house"><span class="c-red">H</span><span class="c-yellow">O</span><span class="c-green">U</span><span class="c-blue">S</span><span class="c-red">E</span></span>
      <span class="headline__line headline__line--painting"><span class="c-yellow">P</span><span class="c-yellow">A</span><span class="c-orange">I</span><span class="c-red">N</span><span class="c-violet">T</span><span class="c-blue">I</span><span class="c-green">N</span><span class="c-yellow">G</span></span>
    </h1>

    <p class="byline">By</p>
    <div class="brand-mark"></div>
    <p class="brand-name">Casa Brightwell</p>
    <p class="web-address">www.casa-brightwell.example</p>

    <div class="color-band color-band--bottom">
      <span class="swatch-orange"></span><span class="swatch-red"></span><span class="swatch-violet"></span><span class="swatch-blue"></span><span class="swatch-green"></span>
    </div>
  </section>
</main>
</body>
</html>
```